EL VARNO EXECUTIVE SERVICE BUSINESS CARDS. FAST

Need business card layout with round logo vs square logo

I have attached a mock up of the business card layout both front and back. I would like to change the square logo to the round logo. And change concierge services on the front of card to guest services. The two yellow highlight circles need to be changed. 1. Please make 1 flower all yellow 2. Please insert unique (use script font) between chief and experience. Use an up sweeping arrow and change to the teal color

Target Market(s)

Transportation

Industry/Entity Type

Transportation

Contact Information for Business Card

Logo large on one side and main business line such as Taxi or executive car service or louisville guest services

Font styles to use
Decorative
Script
Other font styles liked:
• See logo especially the A In the logo

Colors
FFF300
FFF600
FEFA6F
FFFEC7
FFFEE8
FFC000
F8CF3A
FAE287
FDF2CF
FEFAEE

Requirements
Must have
• Logo Cool clean sophisticated design. Phone number list of services.
Nice to have
• Love the black with teal design but instead of vertical, please run line horizontal with a yellow flower splash/dot like the design
Should not have
• Childish animation.

```html
<!DOCTYPE html>
<html lang="en">
<head>
<meta charset="utf-8">
<title>El Varno Executive Service – Business Cards</title>
<link href="https://fonts.googleapis.com/css2?family=Roboto:wght@700&family=Source+Sans+3:wght@400;600&display=swap" rel="stylesheet">
<style>
  :root {
    --stage: #2a2a2b;
    --card: #121212;
    --card-edge: #1b1b1b;
    --gold: #e2b955;
    --gold-soft: #f3d27a;
    --silver: #bdbdbd;
    --white: #f2f2f2;
    --pattern-dark: #15140f;
    --pattern-mid: #221f17;
    --pattern-light: #2e2a1e;
  }
  * { box-sizing: border-box; margin: 0; padding: 0; }
  html, body { width: 1200px; height: 874px; overflow: hidden; }
  body {
    background: var(--stage);
    font-family: "Source Sans 3", Arial, sans-serif;
    position: relative;
  }
  .card {
    position: absolute;
    width: 600px;
    height: 343px;
    border-radius: 22px;
    background: var(--card);
    border: 1px solid var(--card-edge);
    overflow: hidden;
  }
  .card--back { left: 300px; top: 74px; }
  .card--front { left: 300px; top: 457px; }

  /* back side: contact */
  .contact {
    position: absolute;
    left: 52px;
    top: 58px;
  }
  .contact__web {
    color: var(--gold);
    font-size: 22px;
    letter-spacing: 0.3px;
    margin-bottom: 6px;
  }
  .services { list-style: none; margin-bottom: 10px; }
  .services li {
    color: var(--white);
    font-size: 17px;
    line-height: 28px;
    padding-left: 16px;
    position: relative;
  }
  .services li::before {
    content: "";
    position: absolute;
    left: 2px;
    top: 12px;
    width: 5px;
    height: 5px;
    border-radius: 50%;
    background: var(--gold);
  }
  .contact__line {
    color: var(--gold);
    font-size: 22px;
    line-height: 26px;
  }

  /* brand name block */
  .brand {
    position: absolute;
    display: flex;
    align-items: center;
    gap: 16px;
    font-weight: 600;
    line-height: 1.15;
    letter-spacing: 1.5px;
  }
  .brand__dot {
    flex: none;
    border-radius: 50%;
    border: 4px solid currentColor;
  }
  .brand--silver {
    right: 28px;
    top: 102px;
    width: 280px;
    color: var(--silver);
    font-size: 24px;
  }
  .brand--silver .brand__dot { width: 96px; height: 96px; }

  /* front side */
  .pattern {
    position: absolute;
    inset: 0;
    background: radial-gradient(ellipse at 50% 42%, var(--pattern-light), var(--pattern-mid) 45%, var(--pattern-dark) 90%);
  }
  .brand--gold {
    left: 50%;
    top: 62px;
    transform: translateX(-50%);
    width: 400px;
    color: var(--gold);
    font-size: 30px;
  }
  .brand--gold .brand__dot { width: 124px; height: 124px; border-width: 5px; }
  .tagline {
    position: absolute;
    left: 0;
    right: 0;
    bottom: 42px;
    text-align: center;
    font-family: "Roboto", Arial, sans-serif;
    font-weight: 700;
    font-size: 27px;
    color: var(--gold-soft);
  }
</style>
</head>
<body>
  <section class="card card--back" aria-label="Business card back">
    <div class="contact">
      <p class="contact__web">www.ElVarnoES.com</p>
      <ul class="services">
        <li>Praesent luptatum</li>
        <li>Nostrud exerci tation</li>
        <li>Ullamcorper suscipit lobortis</li>
        <li>Dignissim qui blandit</li>
      </ul>
      <p class="contact__line">555.014.2286</p>
      <p class="contact__line">info@ElVarnoES.com</p>
    </div>
    <div class="brand brand--silver">
      <span class="brand__dot"></span>
      <span>EL VARNO EXECUTIVE SERVICE</span>
    </div>
  </section>

  <section class="card card--front" aria-label="Business card front">
    <div class="pattern" role="img" aria-label="Repeating pattern of small dark gold roses across the card"></div>
    <div class="brand brand--gold">
      <span class="brand__dot"></span>
      <span>EL VARNO EXECUTIVE SERVICE</span>
    </div>
    <p class="tagline">Executive Car Service With List of Services</p>
  </section>
</body>
</html>
```